Real eatate

My company name is “Silver Heron Realestate” i would like to create a business card. I would like something modern and sleek similar to picture uploaded. All text in the business card should be black and the logo gold any shade.

```html
<!DOCTYPE html>
<html lang="en">
<head>
<meta charset="utf-8">
<title>Silver Heron Realestate – Business Card</title>
<link rel="stylesheet" href="https://fonts.googleapis.com/css2?family=Figtree:wght@400;600;700&display=swap">
<style>
  :root {
    --page-bg: #d9d3ca;
    --card-top: #f4f3f1;
    --card-bottom: #e4e2de;
    --text-black: #111111;
    --gold: #c99a2e;
    --gold-light: #e2bd57;
    --gold-deep: #a87a22;
  }
  * { box-sizing: border-box; margin: 0; padding: 0; }
  html, body {
    width: 1200px; height: 969px; overflow: hidden;
    background: var(--page-bg);
    font-family: "Figtree", "Helvetica Neue", Arial, sans-serif;
  }
  .business-card {
    position: absolute; left: 75px; top: 185px;
    width: 1050px; height: 600px;
    border-radius: 30px; overflow: hidden;
    background: linear-gradient(160deg, var(--card-top) 0%, #eceae7 55%, var(--card-bottom) 100%);
    box-shadow: 0 2px 10px rgba(0,0,0,0.12);
  }
  .emblem-area {
    position: absolute; left: 20px; top: 20px;
    width: 680px; height: 570px;
    background:
      radial-gradient(ellipse 42% 48% at 38% 55%, var(--gold-light) 0%, var(--gold) 45%, rgba(201,154,46,0.35) 72%, rgba(201,154,46,0) 100%);
  }
  .card-text { position: absolute; right: 57px; top: 0; width: 560px; text-align: right; color: var(--text-black); }
  .card-text > * { position: absolute; right: 0; white-space: nowrap; }
  .brand-name { top: 62px; font-size: 78px; font-weight: 700; letter-spacing: 0.5px; line-height: 1; }
  .brand-sub  { top: 146px; font-size: 30px; font-weight: 700; letter-spacing: 0.4px; line-height: 1; }
  .person-name { top: 198px; font-size: 32px; font-weight: 700; letter-spacing: 0.6px; }
  .person-role { top: 240px; font-size: 21px; letter-spacing: 0.5px; }
  .company-legal { top: 286px; font-size: 21px; }
  .address-line { font-size: 21px; letter-spacing: 0.4px; }
  .address-line.first { top: 316px; }
  .address-line.second { top: 346px; }
  .contact-list { top: 396px; list-style: none; }
  .contact-list li {
    display: flex; justify-content: flex-end; align-items: center; gap: 12px;
    height: 30px; font-size: 21px; letter-spacing: 0.4px; color: var(--text-black);
  }
  .contact-icon { width: 18px; height: 18px; fill: var(--gold-deep); flex: none; }
</style>
</head>
<body>
  <div class="business-card">
    <div class="emblem-area" role="img" aria-label="Large gold brand emblem artwork"></div>

    <div class="card-text">
      <div class="brand-name">SILVER</div>
      <div class="brand-sub">HERON REALESTATE</div>

      <div class="person-name">DANIEL BROOKS</div>
      <div class="person-role">President</div>

      <div class="company-legal">Silver Heron Realestate LLC</div>
      <div class="address-line first">4120 Willow Crest Drive</div>
      <div class="address-line second">Juneau, Alaska 34680</div>

      <ul class="contact-list">
        <li>369-408-1172
          <svg class="contact-icon" viewBox="0 0 24 24" aria-hidden="true"><path d="M6.6 10.8a15.1 15.1 0 0 0 6.6 6.6l2.2-2.2a1 1 0 0 1 1-.25 11.4 11.4 0 0 0 3.6.57 1 1 0 0 1 1 1V20a1 1 0 0 1-1 1A17 17 0 0 1 3 4a1 1 0 0 1 1-1h3.5a1 1 0 0 1 1 1c0 1.25.2 2.45.57 3.6a1 1 0 0 1-.25 1z"/></svg>
        </li>
        <li>369-730-2264
          <svg class="contact-icon" viewBox="0 0 24 24" aria-hidden="true"><path d="M7 2h10a2 2 0 0 1 2 2v16a2 2 0 0 1-2 2H7a2 2 0 0 1-2-2V4a2 2 0 0 1 2-2zm0 3v13h10V5zm4 14.2h2v1.3h-2z"/></svg>
        </li>
        <li>369-615-9043
          <svg class="contact-icon" viewBox="0 0 24 24" aria-hidden="true"><path d="M7 3h10v5H7zM4 9h16a2 2 0 0 1 2 2v6h-3v4H5v-4H2v-6a2 2 0 0 1 2-2zm3 7v3h10v-3z"/></svg>
        </li>
        <li>info@silverheron.com
          <svg class="contact-icon" viewBox="0 0 24 24" aria-hidden="true"><path d="M2 5h20v14H2zm2 2v.5l8 5 8-5V7zm0 3v7h16v-7l-8 5z"/></svg>
        </li>
        <li>www.silverheron.com
          <svg class="contact-icon" viewBox="0 0 24 24" aria-hidden="true"><circle cx="12" cy="12" r="10"/></svg>
        </li>
      </ul>
    </div>
  </div>
</body>
</html>
```